Design some Business Cards

Create a set of business cards for council of Marrowden.
The cards should be somehow indicative of the level/ status age group of the members, which i why a small description of the stages is included.
The card should look professional and colours and designs should match or complement the initial scheme.

```html
<!DOCTYPE html>
<html lang="en">
<head>
<meta charset="utf-8">
<title>Council of Marrowden — Business Cards</title>
<link rel="stylesheet" href="https://fonts.googleapis.com/css2?family=Arimo:wght@400;700&family=Roboto+Condensed:wght@400;700&display=swap">
<style>
  :root {
    --backdrop: #e9e6e1;
    --card-dark: #262424;
    --card-light: #ffffff;
    --brand-green: #6e8f6c;
    --leaf-green: #8dbb4a;
    --name-green: #5b7c5a;
    --stage-founder-start: #4f7a4f;
    --stage-founder-end: #9cc08a;
    --ink: #2b2b2b;
    --white-text: #f2f2f2;
    --faint-ring: #e4ecd9;
  }
  * { margin: 0; padding: 0; box-sizing: border-box; }
  html, body {
    width: 1200px; height: 1200px; overflow: hidden;
    background: var(--backdrop);
  }
  .canvas { position: relative; width: 1200px; height: 1200px; }

  .card {
    position: absolute;
    box-shadow: 0 14px 28px rgba(0,0,0,0.25);
  }
  .card--front {
    left: 217px; top: 120px; width: 755px; height: 431px;
    background: var(--card-dark);
  }
  .card--back {
    left: 220px; top: 613px; width: 756px; height: 431px;
    background: var(--card-light);
  }

  .brand {
    position: absolute;
    display: flex; align-items: center;
    font-family: "Arimo", sans-serif; font-weight: 400;
    color: var(--brand-green);
    white-space: nowrap;
  }
  .brand__dot {
    border: 5px solid var(--leaf-green); border-radius: 50%;
    flex: none;
  }
  .card--front .brand {
    left: 0; right: 0; top: 160px; justify-content: center;
    font-size: 38px; gap: 16px;
  }
  .card--front .brand__dot { width: 70px; height: 70px; }
  .front__web {
    position: absolute; left: 0; right: 0; top: 382px;
    text-align: center;
    font-family: "Arimo", sans-serif; font-size: 16px; letter-spacing: 1.5px;
    color: var(--white-text);
  }

  .card--back .brand {
    left: 40px; top: 56px; font-size: 21px; gap: 10px;
  }
  .card--back .brand__dot { width: 44px; height: 44px; border-width: 3px; }

  /* Member stage marker: colour band indicates the holder's level */
  .holder__stage {
    position: absolute; left: 0; top: 187px; width: 37px; height: 28px;
    background: linear-gradient(90deg, var(--stage-founder-start), var(--stage-founder-end));
  }
  .holder__name {
    position: absolute; left: 44px; top: 182px;
    font-family: "Roboto Condensed", sans-serif; font-weight: 700;
    font-size: 34px; color: var(--name-green); letter-spacing: 0.3px;
  }
  .holder__role {
    position: absolute; left: 44px; top: 224px;
    font-family: "Arimo", sans-serif; font-size: 18px; color: var(--ink);
    letter-spacing: 0.5px;
  }

  .contact {
    position: absolute; left: 44px; top: 295px; list-style: none;
    font-family: "Arimo", sans-serif; font-size: 17px; color: var(--ink);
  }
  .contact li { display: flex; align-items: center; gap: 12px; height: 29.5px; }
  .contact svg { width: 16px; height: 16px; fill: var(--brand-green); flex: none; }

  .address {
    position: absolute; left: 545px; top: 322px;
    font-family: "Arimo", sans-serif; font-style: normal; font-size: 14.5px; line-height: 26px;
    letter-spacing: 1.3px; color: var(--ink);
  }

  .back__ring {
    position: absolute; left: 493px; top: 36px; width: 232px; height: 236px;
    border: 6px solid var(--faint-ring); border-radius: 50%;
  }
</style>
</head>
<body>
<main class="canvas">
  <section class="card card--front">
    <div class="brand"><span class="brand__dot"></span><span>council of Marrowden</span></div>
    <p class="front__web">www.marrowdencouncil.org</p>
  </section>

  <section class="card card--back">
    <div class="brand"><span class="brand__dot"></span><span>council of Marrowden</span></div>
    <div class="back__ring"></div>

    <div class="holder__stage" role="img" aria-label="Member stage marker: founder level"></div>
    <h1 class="holder__name">MARA ELLISON</h1>
    <p class="holder__role">FOUNDER</p>

    <ul class="contact">
      <li>
        <svg viewBox="0 0 16 16" aria-hidden="true"><path d="M4 1h8a1 1 0 0 1 1 1v12a1 1 0 0 1-1 1H4a1 1 0 0 1-1-1V2a1 1 0 0 1 1-1zm0.8 1.8v9.4h6.4V2.8zM8 12.8a.8.8 0 1 0 0 1.6.8.8 0 0 0 0-1.6z"/></svg>
        01 23 456 78
      </li>
      <li>
        <svg viewBox="0 0 16 16" aria-hidden="true"><path d="M8 1a7 7 0 1 0 0 14A7 7 0 0 0 8 1zm0 1.5c.9 0 1.9 1.7 2.2 4.5H5.8C6.1 4.2 7.1 2.5 8 2.5zM2.6 8.5h1.8c.1 1.8.5 3.3 1.1 4.4A5.5 5.5 0 0 1 2.6 8.5zm0-1.5a5.5 5.5 0 0 1 2.9-3.9C4.9 4.2 4.5 5.5 4.4 7zm5.4 6.5c-.9 0-1.9-1.7-2.2-5h4.4c-.3 3.3-1.3 5-2.2 5zm2.5-.6c.6-1.1 1-2.6 1.1-4.4h1.8a5.5 5.5 0 0 1-2.9 4.4zM11.6 7c-.1-1.5-.5-2.8-1.1-3.9A5.5 5.5 0 0 1 13.4 7z"/></svg>
        www.marrowdencouncil.org
      </li>
      <li>
        <svg viewBox="0 0 16 16" aria-hidden="true"><path d="M1 3h14v10H1zm1.5 1.2v.3L8 8.3l5.5-3.8v-.3zm0 2.1v5.5h11V6.3L8 10.1z"/></svg>
        hello@marrowdencouncil.org
      </li>
    </ul>

    <address class="address">41 Larch Street<br>Marrowden MD 20415</address>
  </section>
</main>
</body>
</html>
```